Camp Brenholt Retreat Brochure

We are looking for someone to design a brochure/flyer that we can use to promote renting our camp facility. We don't have a specific size in mind, we are open to different options.

The link below has pictures that can be used (don't expect you to use all of them). It also has a PDF of the information that will need to be included in the brochure.

https://files.quenlark.example/share/7TrK2-PwZn9-LhQa4-XcV3?view=open

We are a Christian camp and retreat facility. You might want to check out our website to get a feel for what we do.

This brochure will be used to help us increase our rental business. Usually given to an organizational leader who is planning a retreat.

Target Market(s)

Church groups, community groups

Industry/Entity Type

Rental

Requirements
Must have
• Pictures
Information that was included
Website
Contact Information
Nice to have
• Logo
Should not have
• Cross
Clip art

```html
<!DOCTYPE html>
<html lang="en">
<head>
<meta charset="utf-8">
<title>Camp Brenholt – Retreat Flyer</title>
<link href="https://fonts.googleapis.com/css2?family=Oswald:wght@500;600&family=Open+Sans:wght@400;700&display=swap" rel="stylesheet">
<style>
  :root {
    --bg: #c9ccd0;
    --paper: #ffffff;
    --green: #17533f;
    --dark: #1c211d;
    --cream: #f3e7a8;
    --orange: #f49a58;
    --ink: #2a2f2b;
  }
  * { margin: 0; padding: 0; box-sizing: border-box; }
  html, body { width: 1200px; height: 1070px; overflow: hidden; background: var(--bg); }
  .flyer {
    position: absolute; left: 220px; top: 43px;
    width: 760px; height: 984px;
    background: var(--paper); overflow: hidden;
    font-family: "Open Sans", sans-serif;
  }
  .flyer-shapes { position: absolute; inset: 0; }
  .brand {
    position: absolute; left: 48px; top: 104px;
    display: flex; align-items: center; gap: 12px;
  }
  .brand-dot { width: 40px; height: 40px; border-radius: 50%; background: var(--orange); }
  .brand-name {
    font-family: "Oswald", sans-serif; font-weight: 600;
    font-size: 28px; letter-spacing: 1px; color: var(--dark); text-transform: uppercase;
  }
  .events { position: absolute; left: 78px; top: 440px; color: #fff; }
  .events-title {
    font-family: "Oswald", sans-serif; font-weight: 500;
    font-size: 40px; letter-spacing: 0.5px; margin-bottom: 6px;
  }
  .events-list { list-style: none; font-size: 19px; line-height: 1.6; }
  .events-list li::before { content: "• "; }
  .booking {
    position: absolute; left: 56px; top: 878px;
    display: flex; align-items: center; gap: 18px; color: #fff;
  }
  .booking-icon {
    width: 64px; height: 64px; border-radius: 50%; background: var(--cream);
    display: flex; align-items: center; justify-content: center;
  }
  .booking-lead { font-size: 17px; }
  .booking-phone { font-weight: 700; font-size: 40px; line-height: 1.05; letter-spacing: 0.5px; }
  .contact { position: absolute; left: 590px; top: 760px; width: 162px; color: var(--ink); }
  .contact-title {
    font-family: "Oswald", sans-serif; font-weight: 600;
    font-size: 22px; color: var(--dark); text-transform: uppercase;
    border-bottom: 2px solid var(--green); padding-bottom: 2px; position: relative;
  }
  .contact-title::after {
    content: ""; position: absolute; left: 0; bottom: -5px;
    width: 34px; height: 4px; background: var(--orange);
  }
  .contact-list { list-style: none; margin-top: 16px; font-size: 11px; line-height: 1.35; }
  .contact-list li { display: flex; gap: 6px; align-items: flex-start; margin-bottom: 9px; white-space: nowrap; }
  .contact-icon { flex: none; width: 15px; height: 15px; }
</style>
</head>
<body>
<main class="flyer">
  <svg class="flyer-shapes" width="760" height="984" viewBox="0 0 760 984">
    <defs>
      <linearGradient id="hall-tones" x1="0" y1="0" x2="1" y2="1">
        <stop offset="0" stop-color="#a9683a"/>
        <stop offset="0.55" stop-color="#7a4a2a"/>
        <stop offset="1" stop-color="#b99480"/>
      </linearGradient>
      <linearGradient id="bunk-tones" x1="0" y1="0" x2="1" y2="1">
        <stop offset="0" stop-color="#d9b27a"/>
        <stop offset="1" stop-color="#9a6a3e"/>
      </linearGradient>
      <linearGradient id="woods-tones" x1="0" y1="0" x2="0" y2="1">
        <stop offset="0" stop-color="#5f7a3a"/>
        <stop offset="0.6" stop-color="#6e5a36"/>
        <stop offset="1" stop-color="#a58a5c"/>
      </linearGradient>
    </defs>
    <circle cx="180" cy="830" r="390" fill="var(--dark)"/>
    <circle cx="262" cy="512" r="324" fill="var(--cream)"/>
    <circle cx="250" cy="500" r="310" fill="var(--green)"/>
    <circle cx="360" cy="0" r="95" fill="var(--orange)"/>
    <circle cx="590" cy="230" r="296" fill="var(--paper)"/>
    <circle cx="590" cy="230" r="290" fill="url(#hall-tones)" role="img" aria-label="Photo of the timber-beamed dining hall with iron chandeliers"/>
    <circle cx="420" cy="390" r="84" fill="var(--paper)"/>
    <circle cx="420" cy="390" r="78" fill="url(#bunk-tones)" role="img" aria-label="Photo of a cabin room with wooden bunk beds"/>
    <circle cx="540" cy="620" r="111" fill="var(--paper)"/>
    <circle cx="540" cy="620" r="105" fill="url(#woods-tones)" role="img" aria-label="Photo of the wooded campgrounds in autumn"/>
  </svg>

  <div class="brand">
    <span class="brand-dot"></span>
    <span class="brand-name">Camp Brenholt</span>
  </div>

  <section class="events">
    <h2 class="events-title">EVENTS</h2>
    <ul class="events-list">
      <li>Church Retreats</li>
      <li>Organizational Meetings</li>
      <li>Boy &amp; Girl Scouts</li>
      <li>School Groups</li>
      <li>Wedding</li>
    </ul>
  </section>

  <section class="booking">
    <span class="booking-icon">
      <svg width="36" height="36" viewBox="0 0 36 36">
        <path d="M5 13c0-4 6-7 13-7s13 3 13 7v2h-7v-3c-2-1-4-1-6-1s-4 0-6 1v3H5z" fill="var(--dark)"/>
        <path d="M10 17h16l4 12H6z" fill="var(--dark)"/>
        <g fill="var(--cream)">
          <circle cx="14" cy="21" r="1.3"/><circle cx="18" cy="21" r="1.3"/><circle cx="22" cy="21" r="1.3"/>
          <circle cx="14" cy="25" r="1.3"/><circle cx="18" cy="25" r="1.3"/><circle cx="22" cy="25" r="1.3"/>
        </g>
      </svg>
    </span>
    <div>
      <p class="booking-lead">To book your retreat call</p>
      <p class="booking-phone">501-555-0142</p>
    </div>
  </section>

  <section class="contact">
    <h2 class="contact-title">Contact Us:</h2>
    <ul class="contact-list">
      <li>
        <svg class="contact-icon" viewBox="0 0 16 16"><circle cx="8" cy="8" r="8" fill="var(--green)"/><path d="M8 3.5a3 3 0 0 1 3 3c0 2.2-3 5.5-3 5.5S5 8.7 5 6.5a3 3 0 0 1 3-3z" fill="#fff"/><circle cx="8" cy="6.5" r="1" fill="var(--green)"/></svg>
        <span>82 Millbrook Hollow Road<br>Harlow, AR 72199</span>
      </li>
      <li>
        <svg class="contact-icon" viewBox="0 0 16 16"><circle cx="8" cy="8" r="8" fill="var(--green)"/><rect x="4" y="5" width="8" height="6" fill="#fff"/><path d="M4 5l4 3.5L12 5" fill="none" stroke="var(--green)" stroke-width="1"/></svg>
        <span>dale@campbrenholt.org</span>
      </li>
      <li>
        <svg class="contact-icon" viewBox="0 0 16 16"><circle cx="8" cy="8" r="8" fill="var(--green)"/><circle cx="8" cy="8" r="4" fill="none" stroke="#fff" stroke-width="1"/><path d="M4 8h8M8 4c-2 2.5-2 5.5 0 8M8 4c2 2.5 2 5.5 0 8" fill="none" stroke="#fff" stroke-width="0.9"/></svg>
        <span>www.campbrenholt.org</span>
      </li>
    </ul>
  </section>
</main>
</body>
</html>
```